Upmarket building and construction company needs signage

Our building company R Brent Construction, needs signage to put up on the side of our vehicle trailers and on site fencing. We are a building company that specialises in residential construction and carpentry .

I will attach our logo and some inspirational pics for site fencing as well as what our trailer looks like .
Other details i would like on the sign are our
( email) rbrentconstruction@mailbox-example.net
(mobile ) 0493 518 264
(website ) rbrentconstruction. example.net

Target Market(s)

Home owners looking for a reliable local builder who produces good quality work. I have attached some inspirational pics.

Industry/Entity Type

Building and Construction

Colors

Designer to choose colors to be used in the design.

Requirements
Must have
• Our logo, contact information
Nice to have
• We would like the design to have elements of being Elegant, Serious, Modern, Professional, Masculine, Conservative and Upmarket.

```html
<!DOCTYPE html>
<html lang="en">
<head>
<meta charset="utf-8">
<title>R Brent Construction – Signage</title>
<link href="https://fonts.googleapis.com/css2?family=Jost:wght@400&display=swap" rel="stylesheet">
<style>
  :root {
    --band-grey: #979797;
    --panel-charcoal: #353535;
    --ink-white: #ffffff;
  }
  html, body {
    margin: 0;
    padding: 0;
    overflow: hidden;
    background: var(--band-grey);
  }
  .sign {
    display: block;
    width: 1200px;
    height: 720px;
    overflow: hidden;
  }
  .sign__band { fill: var(--band-grey); }
  .sign__panel { fill: var(--panel-charcoal); }
  .sign text {
    font-family: "Jost", "Futura", sans-serif;
    font-weight: 400;
    fill: var(--ink-white);
  }
  .brand__name { font-size: 136px; }
  .brand__line { font-size: 66px; }
  .tagline { font-size: 40px; }
  .contact__email, .contact__web { font-size: 32px; }
  .contact__phone { font-size: 37px; }
  .contact__divider { fill: var(--ink-white); }
</style>
</head>
<body>
  <svg class="sign" viewBox="0 0 1200 720" width="1200" height="720" role="img" aria-label="R Brent Construction, Building and Carpentry">
    <rect class="sign__band" x="0" y="0" width="1200" height="720"/>
    <rect class="sign__panel" x="0" y="26" width="1200" height="668"/>

    <text class="brand__name" x="330" y="403" textLength="538" lengthAdjust="spacing">R BRENT</text>
    <text class="brand__line" x="330" y="482" textLength="540" lengthAdjust="spacing">CONSTRUCTION</text>
    <text class="tagline" x="330" y="537" textLength="540" lengthAdjust="spacing">BUILDING AND CARPENTRY</text>

    <text class="contact__email" x="57" y="648" textLength="413" lengthAdjust="spacingAndGlyphs">rbrentconstruction@mailbox-example.net</text>
    <rect class="contact__divider" x="488" y="622" width="2.5" height="26"/>
    <text class="contact__phone" x="513" y="648" textLength="231" lengthAdjust="spacing">0493 518 264</text>
    <rect class="contact__divider" x="768" y="622" width="2.5" height="26"/>
    <text class="contact__web" x="797" y="648" textLength="347" lengthAdjust="spacingAndGlyphs">rbrentconstruction.example.net</text>
  </svg>
</body>
</html>
```